Cookbook - Book Cover Contest

Title: 40 Suppers Worth Sharing Around Town - A Neighborly Gratitude Kitchen Book
Dimensions: 8x5 x 8x5 inches
FRONT AND BACK COVER SEPARATE / NO SPINE
Final Formats: png, jpg, pdf, ai/vector + Layers & Fonts

Description:
I would like the part of the title that says "40 Suppers Worth Sharing Around Town" to be the main and bigger title and the smaller, secondary title "A Neighborly Gratitude Kitchen Book". I want to have a beautiful cover with the theme of teachers, school, chalkboard but I want it to be clear it is a cookbook. I want the title to be big and eye-catching, easy to read. The colors should be unisex, fun, and vibrant. Please do not make it too busy and hard to read. The cookbook is American style, so seafood and meat are included but please do not add your own pictures of food. I added two images, you're NOT required to use them as I do want a more chalkboard style cover to match the interior of the book.
I do NOT want real pictures of teachers or people on the cookbook cover.

If you have questions, please just let me know!

```html
<!DOCTYPE html>
<html lang="en">
<head>
<meta charset="utf-8">
<title>40 Suppers Worth Sharing Around Town – Cover</title>
<link rel="stylesheet" href="https://fonts.googleapis.com/css2?family=Roboto:wght@300;700&display=swap">
<style>
  :root {
    --backdrop: #17120f;
    --orange: #ef6a24;
    --ink: #262626;
    --panel: #ffffff;
    --rule: #8f8f8f;
    --slate-dark: #1c1b1b;
    --slate-mid: #2c2927;
    --spice-red: #7a2a1c;
    --salt: #6e6a66;
    --oil: #6b4a1c;
    --wood-light: #9a4e2a;
    --wood-dark: #4d2414;
  }
  * { box-sizing: border-box; margin: 0; padding: 0; }
  html, body {
    width: 1200px;
    height: 1183px;
    overflow: hidden;
    background: var(--backdrop);
  }
  .cover {
    position: absolute;
    left: 156px;
    top: 148px;
    width: 887px;
    height: 885px;
    background: var(--slate-dark);
    overflow: hidden;
  }
  .cover__photo {
    position: absolute;
    left: 0;
    top: 0;
    width: 435px;
    height: 100%;
    background:
      radial-gradient(circle at 35% 14%, var(--spice-red) 0%, transparent 14%),
      radial-gradient(circle at 37% 34%, var(--salt) 0%, transparent 13%),
      radial-gradient(circle at 68% 22%, var(--oil) 0%, transparent 16%),
      radial-gradient(circle at 18% 85%, #8d7c74 0%, transparent 16%),
      radial-gradient(ellipse at 75% 80%, var(--wood-light) 0%, transparent 38%),
      linear-gradient(160deg, var(--slate-mid), var(--slate-dark));
  }
  .cover__board {
    position: absolute;
    left: 835px;
    top: 0;
    width: 52px;
    height: 100%;
    background: linear-gradient(180deg, var(--slate-dark) 0%, var(--slate-dark) 20%, var(--wood-light) 20.5%, var(--wood-dark) 100%);
  }
  .title-panel {
    position: absolute;
    left: 435px;
    top: 0;
    width: 400px;
    height: 100%;
    background: var(--panel);
    font-family: "Roboto", Arial, sans-serif;
    color: var(--ink);
  }
  .title-frame {
    position: absolute;
    left: 30px;
    top: 156px;
    width: 339px;
    height: 225px;
    border: 3px solid var(--orange);
  }
  .centered {
    position: absolute;
    left: 50%;
    transform: translate(-50%, -50%);
    text-align: center;
    white-space: nowrap;
    line-height: 1;
  }
  .title-number {
    top: 262px;
    font-size: 240px;
    font-weight: 700;
    color: var(--orange);
    letter-spacing: -6px;
  }
  .title-word {
    top: 381px;
    font-size: 62px;
    font-weight: 700;
    color: var(--orange);
    letter-spacing: -1px;
    background: var(--panel);
    padding: 0 10px;
  }
  .subtitle,
  .tagline {
    font-size: 35px;
    font-weight: 300;
    line-height: 45px;
    text-transform: uppercase;
  }
  .subtitle { top: 512px; }
  .tagline { top: 687px; }
  .divider {
    position: absolute;
    left: 62px;
    top: 615px;
    width: 278px;
    height: 2px;
    background: var(--rule);
  }
</style>
</head>
<body>
  <div class="cover">
    <div class="cover__photo" role="img" aria-label="Cookbook photo: bowls of peppercorns, sea salt and olive oil with rosemary, a red chili, bay leaf, garlic bulbs and wooden spoons on a dark slate board"></div>
    <div class="cover__board" role="img" aria-label="Edge of a wooden cutting board"></div>

    <section class="title-panel">
      <div class="title-frame"></div>
      <h1>
        <span class="centered title-number">40</span>
        <span class="centered title-word">SUPPERS</span>
      </h1>
      <p class="centered subtitle">A Neighborly<br>Gratitude<br>Kitchen Book</p>
      <div class="divider"></div>
      <p class="centered tagline">Worth Sharing<br>Around Town</p>
    </section>
  </div>
</body>
</html>
```